Book Title: The Harbor's Lantern. Author Name: Marisol Thackeray

We are needing a cover, spine and back cover design for a poetry book that we are publishing called The Harbor's Lantern. We are looking for an elegant, and simplistic design with a very natural, dynamic and powerful impact.

Design Idea #1 - Shiva Conch Shell with a pink or black background. See Glen Parvey Image attached for design inspiration. Simple and dynamic .
Title and Author name created in same style as the attached Glen Parvey's Lanterns and Driftwood image.

Design Idea #2 - Image of cauldron on (see cauldrons attached for ideas) black background.
See Glen Parvey Image attached for design inspiration. Simple and dynamic Title and Author name created in same style as the attached Glen Parvey's Lanterns and Driftwood image

Design Idea #3 - Image of Tree of Life (see attached images for idea of what we are looking for) Would like to see on plain white, green, black and green background.

Target Market(s)

Spiritual Women, healers, visionaries,Goddess'

Requirements
Must have
• Please see project descriptions for specific design concepts we are looking for. Please include the authors name: Marisol Thackeray on front, spine and back cover of the book

```html
<!DOCTYPE html>
<html lang="en">
<head>
<meta charset="utf-8">
<title>The Harbor's Lantern — Book Cover Spread</title>
<link rel="stylesheet" href="https://fonts.googleapis.com/css2?family=Cinzel:wght@400;500;600&family=Tinos:wght@400;700&family=Lato:wght@400&display=swap">
<style>
  :root {
    --page-bg: #ffffff;
    --cover-bg: #030303;
    --ink-light: #ffffff;
    --ink-spine: #111111;
    --green-deep: #5f8a34;
    --green-mid: #8fb25a;
    --green-sage: #9cbf8c;
    --green-bright: #8ab43d;
    --placeholder: #ffffff;
  }
  * { margin: 0; padding: 0; box-sizing: border-box; }
  html, body {
    width: 1200px; height: 1200px; overflow: hidden;
    background: var(--page-bg);
  }
  .spread {
    position: absolute; left: 41px; top: 196px;
    width: 1125px; height: 815px;
    background: var(--cover-bg);
  }
  .panel { position: absolute; top: 0; height: 100%; }
  .back-cover { left: 0; width: 540px; }
  .spine {
    left: 540px; width: 45px;
    background: linear-gradient(180deg, var(--green-sage) 0%, var(--green-bright) 30%, var(--green-sage) 60%, var(--green-bright) 85%, var(--green-deep) 100%);
  }
  .front-cover { left: 585px; width: 540px; }

  .title {
    position: absolute; left: 0; width: 100%; text-align: center;
    font-family: "Cinzel", serif; font-weight: 500; line-height: 1;
  }
  .title-the {
    display: flex; align-items: center; justify-content: center; gap: 14px;
    color: var(--ink-light);
  }
  .title-the::before, .title-the::after {
    content: ""; display: block; height: 2px;
    background: linear-gradient(90deg, transparent, var(--ink-light), transparent);
  }
  .title-main {
    background: linear-gradient(90deg, var(--green-deep), var(--green-sage) 35%, var(--green-bright) 65%, var(--green-sage) 85%, var(--green-bright));
    -webkit-background-clip: text; background-clip: text; color: transparent;
    font-weight: 600;
  }
  .title-sub { color: var(--ink-light); }

  /* back cover */
  .back-cover .title-the { top: 47px; font-size: 29px; }
  .back-cover .title-the::before, .back-cover .title-the::after { width: 48px; }
  .back-cover .title-main { top: 82px; font-size: 52px; }
  .back-cover .title-sub { top: 137px; font-size: 52px; }

  .blurb, .bio-text {
    font-family: "Lato", sans-serif; color: var(--ink-light);
    font-size: 12.3px; line-height: 14.4px; text-align: justify;
  }
  .blurb { position: absolute; left: 49px; top: 204px; width: 458px; }
  .divider {
    position: absolute; left: 189px; top: 378px; width: 176px; height: 3px;
    background: linear-gradient(90deg, var(--green-deep), var(--green-mid));
  }
  .author-photo { position: absolute; left: 49px; top: 413px; width: 113px; height: 150px; background: var(--placeholder); }
  .bio { position: absolute; left: 174px; top: 411px; width: 332px; }
  .bio-name {
    font-family: "Tinos", serif; font-weight: 700; color: var(--ink-light);
    font-size: 18.5px; line-height: 1; margin-bottom: 10px; letter-spacing: 0.3px;
  }
  .tree-emblem {
    position: absolute; left: 50px; top: 654px; width: 118px; height: 112px;
    background: radial-gradient(closest-side, var(--green-bright) 0%, var(--green-mid) 45%, var(--green-deep) 75%, transparent 100%);
  }
  .barcode-area { position: absolute; left: 312px; top: 652px; width: 192px; height: 115px; background: var(--placeholder); }

  /* spine */
  .spine-title, .spine-author {
    position: absolute; left: 0; width: 45px;
    writing-mode: vertical-rl; display: flex; align-items: center;
    color: var(--ink-spine);
  }
  .spine-title { top: 48px; height: 410px; font-family: "Cinzel", serif; font-size: 25px; letter-spacing: 1.6px; }
  .spine-emblem {
    position: absolute; left: 10px; top: 479px; width: 25px; height: 25px;
    background: radial-gradient(closest-side, #1d2a14 0%, #2a3a1e 60%, transparent 100%);
  }
  .spine-author { top: 528px; height: 240px; font-family: "Tinos", serif; font-size: 25px; letter-spacing: 0.3px; }

  /* front cover */
  .front-cover .title-the { top: 43px; font-size: 46px; gap: 18px; }
  .front-cover .title-the::before, .front-cover .title-the::after { width: 75px; }
  .front-cover .title-main { top: 98px; font-size: 80px; }
  .front-cover .title-sub { top: 184px; font-size: 80px; }
  .tree-illustration {
    position: absolute; left: 74px; top: 313px; width: 382px; height: 363px;
    background: radial-gradient(closest-side, var(--green-bright) 0%, var(--green-mid) 40%, var(--green-deep) 72%, transparent 100%);
  }
  .front-author {
    position: absolute; left: 0; width: 100%; top: 726px; text-align: center;
    font-family: "Tinos", serif; color: var(--ink-light); font-size: 45px; line-height: 1;
  }
</style>
</head>
<body>
  <main class="spread">
    <section class="panel back-cover">
      <div class="title title-the">THE</div>
      <div class="title title-main">HARBOR'S</div>
      <div class="title title-sub">LANTERN</div>
      <p class="blurb">Lorem ipsum dolor sit amet, consectetur adipiscing elit. Curabitur laoreet viverra bibendum. Proin eleifend varius tellus a ultrices. Donec feugiat, leo ut egestas auctor, nunc purus placerat sem, non molestie odio orci at felis. In hac habitasse platea dictumst. Sed a diam vitae ex ornare pellentesque vel eu nisl. Praesent pharetra in nibh quis ultricies. Duis viverra maximus mattis. Donec purus eros, pulvinar non nulla id, porta maximus enim. Nam vestibulum vestibulum massa, quis fermentum nisi aliquet a. Vestibulum eget nunc purus placerat sem, non molestie odio orci at felis. Proin eleifend varius tellus a ultrices. Donec feugiat, leo ut egestas auctor, nunc purus placerat pellentesque vel eu nisl. Praesent pharetra in nibh quis ultricies. Duis viverra maximus mattis.</p>
      <div class="divider"></div>
      <div class="author-photo" role="img" aria-label="Author portrait placeholder"></div>
      <div class="bio">
        <h2 class="bio-name">MARISOL THACKERAY</h2>
        <p class="bio-text">Lorem ipsum dolor sit amet, consectetur adipiscing elit. Curabitur laoreet viverra bibendum. Proin eleifend varius tellus a ultrices. Donec feugiat, leo ut egestas auctor, nunc purus placerat sem, non molestie odio orci at felis. In hac habitasse platea dictumst. Sed a diam vitae ex ornare pellentesque vel eu nisl. Praesent pharetra in nibh quis ultricies. Duis viverra maximus mattis. Donec purus eros, pulvinar non nulla id, porta maximus enim. Nam vestibulum vestibulum massa, quis fermentum nisi aliquet</p>
      </div>
      <div class="tree-emblem" role="img" aria-label="Small green tree of life illustration"></div>
      <div class="barcode-area"></div>
    </section>

    <section class="panel spine">
      <div class="spine-title">THE HARBOR'S LANTERN</div>
      <div class="spine-emblem" role="img" aria-label="Small tree of life emblem"></div>
      <div class="spine-author">Marisol Thackeray</div>
    </section>

    <section class="panel front-cover">
      <div class="title title-the">THE</div>
      <h1 class="title title-main">HARBOR'S</h1>
      <div class="title title-sub">LANTERN</div>
      <div class="tree-illustration" role="img" aria-label="Green watercolour tree of life with leafy curling branches and small butterflies"></div>
      <div class="front-author">Marisol Thackeray</div>
    </section>
  </main>
</body>
</html>
```